The Drifters

Amber Hawks Productions is looking for their theatrical poster for their film 'THE DRIFTERS'... It is a zombie appocalypse action film made in NSW Australia. See their facebook page www.facebook.com/THEDRIFTERSFILM...
Updates
Project Deadline Extended
Reason: i have decided to EXTEND the deadline for 5 more days, as there are some really talented artists reviewing their submissions for us... Thank you to all...
Please review the new uploaded images you may or may not want to use to revierw your submissions
Logo Text
Amber Hawks Productions
Look and feel
Each slider illustrates characteristics of the customer's brand and the style your logo design should communicate.

```html
<!DOCTYPE html>
<html lang="en">
<head>
<meta charset="utf-8">
<title>The Drifters – Theatrical Poster</title>
<link rel="stylesheet" href="https://fonts.googleapis.com/css2?family=Anton&family=Cinzel:wght@400;500&family=Oswald:wght@400;500&display=swap">
<style>
  :root {
    --paper: #eeeeee;
    --paper-edge: #d9d9d9;
    --blood: #d9202a;
    --blood-deep: #b8141d;
    --ink: #0d0d0d;
    --ink-soft: #1c1c1c;
    --credit-on-red: #8e1016;
    --gap: #ffffff;
  }
  * { box-sizing: border-box; margin: 0; padding: 0; }
  html, body {
    width: 1200px; height: 889px; overflow: hidden;
    background: var(--gap);
  }
  .poster-set {
    position: relative; width: 1200px; height: 889px;
    display: flex; justify-content: space-between;
  }
  .poster {
    position: relative; width: 598px; height: 889px; overflow: hidden;
    text-align: center;
  }
  .poster--light {
    background: radial-gradient(ellipse at 50% 45%, #f7f7f7 0%, var(--paper) 60%, var(--paper-edge) 100%);
  }
  .poster--red {
    background: radial-gradient(ellipse at 50% 45%, #e2262f 0%, var(--blood) 55%, var(--blood-deep) 100%);
  }
  .tagline {
    position: absolute; top: 34px; left: 0; width: 100%;
    font-family: 'Cinzel', serif; font-weight: 400;
    font-size: 19px; letter-spacing: 3px; color: var(--ink-soft);
  }
  .portrait {
    position: absolute; left: 100px; top: 92px; width: 400px; height: 560px;
    background: radial-gradient(ellipse 46% 52% at 50% 46%, var(--ink) 0%, var(--ink) 70%, rgba(13,13,13,0.55) 88%, rgba(13,13,13,0) 100%);
  }
  .title {
    position: absolute; left: 0; width: 100%;
    font-family: 'Anton', sans-serif; color: var(--ink);
    line-height: 1; text-transform: uppercase;
  }
  .title__the { top: 592px; font-size: 64px; letter-spacing: 1px; }
  .title__name { top: 660px; font-size: 84px; letter-spacing: 0; }
  .splatter {
    position: absolute; left: 86px; top: 696px; width: 70px; height: 36px;
    border-radius: 50% 45% 55% 40%;
  }
  .poster--light .splatter { background: var(--blood); }
  .poster--red .splatter { background: #ffffff; }
  .release {
    position: absolute; top: 772px; left: 0; width: 100%;
    font-family: 'Cinzel', serif; font-size: 13px; letter-spacing: 3px;
    color: var(--ink-soft);
  }
  .credits {
    position: absolute; top: 806px; left: 0; width: 100%;
    font-family: 'Oswald', sans-serif; font-weight: 500;
    font-size: 11px; line-height: 15px; letter-spacing: 0.3px;
    color: var(--ink-soft); text-transform: uppercase;
  }
  .poster--red .credits { color: var(--credit-on-red); }
  .credits__role { font-size: 6px; letter-spacing: 0; vertical-align: middle; }
</style>
</head>
<body>
<main class="poster-set">

  <section class="poster poster--light">
    <p class="tagline">IT’S KILL OR BE KILLED</p>
    <div class="portrait" role="img" aria-label="Dark silhouette portrait of a young man with glowing red eyes"></div>
    <h1 class="title title__the">THE</h1>
    <h1 class="title title__name">DRIFTERS</h1>
    <div class="splatter" role="img" aria-label="Red blood splatter"></div>
    <p class="release">COMING SOON</p>
    <div class="credits">
      <p>Amber Hawks Productions <span class="credits__role">presents</span> The Drifters <span class="credits__role">a film by</span> Darcy Quinlan <span class="credits__role">produced by</span> Darcy Quinlan</p>
      <p>Darcy Quinlan &nbsp;Tomas Bellucci &nbsp;Sienna Marlowe <span class="credits__role">edited by</span> Callum Reeves <span class="credits__role">music by</span> Owen Hartley</p>
      <p><span class="credits__role">visual effects</span> Callum Reeves <span class="credits__role">assistant director</span> Jonah Pelling <span class="credits__role">associate producer</span> Ivy Fairbanks <span class="credits__role">written and directed by</span> Darcy Quinlan</p>
      <p><span class="credits__role">make up by</span> Harriet Cole &nbsp;Tayla Winslow &nbsp;Naomi Prescott &nbsp;June Ashcroft</p>
    </div>
  </section>

  <section class="poster poster--red">
    <p class="tagline">IT’S KILL OR BE KILLED</p>
    <div class="portrait" role="img" aria-label="Dark silhouette portrait of a young man with glowing red eyes"></div>
    <h1 class="title title__the">THE</h1>
    <h1 class="title title__name">DRIFTERS</h1>
    <div class="splatter" role="img" aria-label="White paint splatter"></div>
    <p class="release">COMING SOON</p>
    <div class="credits">
      <p>Amber Hawks Productions <span class="credits__role">presents</span> The Drifters <span class="credits__role">a film by</span> Darcy Quinlan <span class="credits__role">produced by</span> Darcy Quinlan</p>
      <p>Darcy Quinlan &nbsp;Tomas Bellucci &nbsp;Sienna Marlowe <span class="credits__role">edited by</span> Callum Reeves <span class="credits__role">music by</span> Owen Hartley</p>
      <p><span class="credits__role">visual effects</span> Callum Reeves <span class="credits__role">assistant director</span> Jonah Pelling <span class="credits__role">associate producer</span> Ivy Fairbanks <span class="credits__role">written and directed by</span> Darcy Quinlan</p>
      <p><span class="credits__role">make up by</span> Harriet Cole &nbsp;Tayla Winslow &nbsp;Naomi Prescott &nbsp;June Ashcroft</p>
    </div>
  </section>

</main>
</body>
</html>
```